Postcard Design Seabright Mews

I need a postcard design to publicise my holiday let in Falmouth. The postcard needs to refer to the location which is 27 Seabright Mews Falmouth and include on the front For bookings or further information visit TWRetreats www.twretreats.co.ukor telephone 01872 938204.The postcard needs to be small size, glossy on one side and conventional on the reverse.The following documents are relevant picture of building and local photo.

```html
<!DOCTYPE html>
<html lang="en">
<head>
<meta charset="utf-8">
<title>27 Seabright Mews Falmouth – Postcard</title>
<link rel="stylesheet" href="https://fonts.googleapis.com/css2?family=Open+Sans:wght@400;600;700&display=swap">
<style>
  :root {
    --brand-blue: #1d62ad;
    --brand-navy: #1f3f8f;
    --brand-light: #4aa3e0;
    --text-grey: #555b63;
    --text-dark: #2f3338;
    --rule-grey: #b9bdc2;
    --card-white: #ffffff;
  }
  * { margin: 0; padding: 0; box-sizing: border-box; }
  html, body { width: 951px; height: 1200px; overflow: hidden; background: var(--card-white); }
  .postcard {
    position: relative;
    width: 951px;
    height: 1200px;
    background: var(--card-white);
    font-family: "Open Sans", Arial, sans-serif;
    overflow: hidden;
  }
  .postcard__art { position: absolute; inset: 0; }
  .postcard__details {
    position: absolute;
    left: 0; right: 0;
    top: 785px;
    text-align: center;
  }
  .details__title {
    font-size: 50px;
    font-weight: 400;
    color: var(--brand-blue);
    line-height: 1.2;
  }
  .details__rule {
    width: 730px;
    height: 2px;
    margin: 14px auto 20px;
    background: var(--rule-grey);
    border: 0;
  }
  .details__info {
    font-size: 33px;
    color: var(--text-grey);
    line-height: 1.28;
  }
  .details__info strong { color: var(--text-dark); font-weight: 700; }
  .details__phone {
    margin-top: 26px;
    display: flex;
    justify-content: center;
    align-items: center;
    gap: 40px;
    font-size: 35px;
    color: var(--text-grey);
  }
  .details__phone-number {
    display: inline-flex;
    align-items: center;
    gap: 16px;
    font-size: 44px;
    font-weight: 700;
    color: var(--brand-blue);
  }
  .details__phone-icon { width: 38px; height: 38px; }
</style>
</head>
<body>
<main class="postcard">
  <svg class="postcard__art" width="951" height="1200" viewBox="0 0 951 1200">
    <defs>
      <linearGradient id="harbourSky" x1="0" y1="0" x2="0" y2="1">
        <stop offset="0" stop-color="#c9dff0"/>
        <stop offset="0.55" stop-color="#dfe9f1"/>
        <stop offset="1" stop-color="#e8edf0"/>
      </linearGradient>
      <linearGradient id="harbourShore" x1="0" y1="0" x2="1" y2="0">
        <stop offset="0" stop-color="#9a9c9c"/>
        <stop offset="0.35" stop-color="#c4c6c8"/>
        <stop offset="0.5" stop-color="#9a7d66"/>
        <stop offset="0.7" stop-color="#5d6470"/>
        <stop offset="1" stop-color="#6c6e70"/>
      </linearGradient>
      <linearGradient id="harbourSea" x1="0" y1="0" x2="0" y2="1">
        <stop offset="0" stop-color="#3f6d98"/>
        <stop offset="0.35" stop-color="#2f5d8b"/>
        <stop offset="1" stop-color="#1f4775"/>
      </linearGradient>
      <radialGradient id="seaGlint" cx="0.35" cy="0.35" r="0.6">
        <stop offset="0" stop-color="#6d97bf" stop-opacity="0.45"/>
        <stop offset="1" stop-color="#6d97bf" stop-opacity="0"/>
      </radialGradient>
      <linearGradient id="buildingTones" x1="0" y1="0" x2="0" y2="1">
        <stop offset="0" stop-color="#4f8fdc"/>
        <stop offset="0.18" stop-color="#9cc2ec"/>
        <stop offset="0.26" stop-color="#eef0f0"/>
        <stop offset="0.7" stop-color="#e2e3df"/>
        <stop offset="0.82" stop-color="#b9bbb5"/>
        <stop offset="0.92" stop-color="#6f8a4f"/>
        <stop offset="1" stop-color="#4c6635"/>
      </linearGradient>
      <linearGradient id="waveBlue" x1="0" y1="0" x2="1" y2="0">
        <stop offset="0" stop-color="var(--brand-light)"/>
        <stop offset="0.5" stop-color="var(--brand-blue)"/>
        <stop offset="1" stop-color="var(--brand-navy)"/>
      </linearGradient>
      <clipPath id="harbourClip"><rect x="0" y="0" width="951" height="720"/></clipPath>
    </defs>

    <g class="harbour-photo" clip-path="url(#harbourClip)" role="img" aria-label="Photo of Falmouth harbour with moored yachts and waterfront buildings">
      <rect class="harbour-photo__sky" x="0" y="0" width="951" height="290" fill="url(#harbourSky)"/>
      <rect class="harbour-photo__shore" x="0" y="250" width="951" height="60" fill="url(#harbourShore)" opacity="0.85"/>
      <rect class="harbour-photo__sea" x="0" y="305" width="951" height="415" fill="url(#harbourSea)"/>
      <rect class="harbour-photo__glint" x="0" y="305" width="951" height="415" fill="url(#seaGlint)"/>
    </g>

    <path class="header-wave" d="M0 575 C220 700 600 700 951 470 L951 1200 L0 1200 Z" fill="url(#waveBlue)"/>
    <path class="header-wave-white" d="M0 665 C260 760 640 700 951 520 L951 1200 L0 1200 Z" fill="var(--card-white)"/>

    <circle class="building-frame" cx="741" cy="560" r="168" fill="var(--brand-blue)"/>
    <circle class="building-frame-inner" cx="741" cy="560" r="162" fill="var(--card-white)"/>
    <circle class="building-photo" cx="741" cy="560" r="152" fill="url(#buildingTones)"
            role="img" aria-label="Photo of the white-fronted terrace house at 27 Seabright Mews"/>

    <path class="corner-swoosh" d="M600 1170 C720 1100 830 1070 951 1055 L951 1070 C830 1085 720 1115 600 1170 Z" fill="url(#waveBlue)"/>
    <rect class="foot-band" x="0" y="1186" width="951" height="14" fill="url(#waveBlue)"/>
  </svg>

  <section class="postcard__details">
    <h1 class="details__title">27 Seabright Mews Falmouth</h1>
    <hr class="details__rule">
    <p class="details__info">For bookings or further information visit<br>TWRetreats <strong>www.twretreats.co.uk</strong></p>
    <p class="details__phone">
      <span class="details__phone-label">Call us on:</span>
      <span class="details__phone-number">
        <svg class="details__phone-icon" viewBox="0 0 24 24" aria-hidden="true">
          <path fill="var(--brand-blue)" d="M6.6 10.8a15.1 15.1 0 0 0 6.6 6.6l2.2-2.2a1 1 0 0 1 1-.25 11.4 11.4 0 0 0 3.6.57 1 1 0 0 1 1 1V20a1 1 0 0 1-1 1A17 17 0 0 1 3 4a1 1 0 0 1 1-1h3.5a1 1 0 0 1 1 1c0 1.25.2 2.45.57 3.6a1 1 0 0 1-.25 1z"/>
          <path fill="none" stroke="var(--brand-blue)" stroke-width="1.8" stroke-linecap="round" d="M14.5 3.5a6.5 6.5 0 0 1 6 6M14 7a3 3 0 0 1 3 3"/>
        </svg>
        01872 938204
      </span>
    </p>
  </section>
</main>
</body>
</html>
```